Template design for micro site for a corporate-branded mobile software product

We need a creative web designer to help us quickly design a template design for a micro site webpage for a product called Korvane Unified Alerts, and we need the template design to be shown in 3 distinct industry designs. The template design shall be a one-page corporate brochure and product page, and the same template design will be re-used for 3 different industry pages. Although the layout and navigation design shall not change, each of the 3 industry pages must have its own unique design/content/look/feel to address specific capabilities of our product that are important to that industry or topic.

NOTE: This is a design project, not a web development project. We will hand your designs over to a web developer.

REQUIRED:
Create a template design that includes Korvane branding guidelines and can be used consistently for each of our 3 different industry micro site web pages (i.e., the template design should consider such things as overall page navigation design & layout design to deliver a common experience for the viewer).

REQUIRED:
In terms of layout, please model your template design after one of the following responsive website layouts, and please indicate which you chose:

http://www.plinththemes.example/gym-fitness-business-wordpress-theme-vigor/
http://www.plinththemes.example/meld-a-sleek-flashy-and-professional-wordpress-theme/
http://www.plinththemes.example/bold-and-modern-responsive-business-wordpress-theme-sprightly/
http://www.plinththemes.example/summit-business-premium-wordpress-theme/
http://themevault.example/themes/tailorix
http://www.plinththemes.example/level-kit-business-portfolio-wordpress-theme/
http://www.plinththemes.example/stillwater-premium-origin-child-theme/

REQUIRED:
Use the template to design 3 unique designs, one for each of the following 3 industry topic pages (you may change anything in the design such as colors, pictures, icons, etc. to create a look/feel relevant for the topic):
- Workplace Harassment & HR
- Financial Institutions
- Mining & Construction (includes Oil, Gas, etc.)

Attached are content ideas for the above 3 industry topics for use in your suggested designs.

REQUIRED: Korvane branding is a requirement (we must use the spectrum design element at top of page). Colors can (probably should) change for each of the 3 micro site designs. You can see examples of Korvane branding at www.korvane.example, www.korvane-kua.example/school, and in the attached PowerPoints.

REQUIRED: We must have a contact us form similar to the form at the bottom of www.korvane-kua.example/school or at the bottom of www.artguild.example. The specific goal of these 3 website designs are to drive sales leads and conversions to request more information from our sales team, so we are seeking a design/layout that helps drive site conversions.

REQUIRED: Navigation menu similar to the one at www.korvane.example (at the top of the page)

Nice to have:

PICTURES: Pictures will definitely need to change for each site. If you can make suggestions on pictures, that will help. We are ok with taking additional (optional) proposals if you find pictures you think really help the site.

Reason: We are looking for a design that really takes the Korvane branding guidelines into careful consideration.

We invite you to design your template based on one of the following responsive layouts, and please indicate to us which one you chose (so we can purchase it and give it to our web developer). Thank you.

Target Market(s)

Each of the 3 industry pages should target each of the following (respectively):
1. Workplace Harassment (general topic)
2. Financial Institutions (Banking, Insurance, Investment, Retail/Corporate)
3. Mining (includes Oil, Gas, and peripherally includes Energy)

See attached PowerPoint file for some content ideas for your design.

Industry/Entity Type

Software

Requirements
Must have
• - Templatte design must be modeled after one of the following layouts

- Template design must be a single page layout. Content should fit into screens of 1366x768, and no "scrolling" should be necessary if the user presses the navigation menu buttons (e.g., see www.korvane-kua.example/school for an example of how the navigation menu takes you to the content without scrolling)
- Each of the 3 micro site industry pages must be different (pictures, content, etc.) but must use the same template design
- Must use Korvane branding guidelines (attached)
- Must include a Contact Us form similar to the bottom of the page at www.korvane-kua.example/school or the bottom of the page at www.artguild.example
- Must include a Navigation Bar at the top similar to www.korvane.example
- Must maintain some consistency (visually and navigation) with existing 2 micro sites already launched (see URLs above)
Nice to have
• - Pictures (it is ok to send a separate proposal for pictures if cost is a concern)
- Visual appeal with professional and modern look/feel
- Consideration for driving site conversions to "Getting Started" and "Request More Info" buttons
- Consideration for responsive web developer
- Consideration for SEO
Should not have
• - Search box

```html
<!DOCTYPE html>
<html lang="en">
<head>
<meta charset="utf-8">
<title>Korvane Unified Alerts – Mining &amp; Construction</title>
<link rel="stylesheet" href="https://fonts.googleapis.com/css2?family=Roboto:wght@300;400;500;700;900&display=swap">
<style>
  :root {
    --blue: #0a6bbf;
    --blue-deep: #0050a0;
    --blue-bright: #00a3e8;
    --blue-sky: #5cc6f2;
    --ink: #222;
    --muted: #666;
    --btn: #555;
    --light: #f6f6f6;
    --topbar: #f2f2f2;
    --footer: #3a3a3a;
    --footer-head: #8c8c8c;
    --footer-text: #a8a8a8;
  }
  * { box-sizing: border-box; margin: 0; padding: 0; }
  html, body { width: 989px; height: 1200px; overflow: hidden; }
  body { font-family: 'Roboto', sans-serif; color: var(--ink); background: #fff; position: relative; }

  .topbar { height: 26px; background: var(--topbar); border-bottom: 1px solid #e4e4e4; position: relative; font-size: 10px; color: #777; }
  .topbar .phone { position: absolute; left: 198px; top: 7px; display: flex; align-items: center; gap: 5px; }
  .topbar .search { position: absolute; left: 166px; top: 0; width: 26px; height: 26px; border-right: 1px solid #e0e0e0; border-left: 1px solid #e0e0e0; display: flex; align-items: center; justify-content: center; }
  .topbar .social-mini { position: absolute; left: 438px; top: 8px; display: flex; gap: 9px; }
  .topbar .social-mini span { width: 10px; height: 10px; border-radius: 50%; background: var(--blue); display: block; }
  .topbar .social-mini span.red { background: #d8452b; }
  .topbar .social-mini span.orange { background: #f07b1d; }
  .topbar .links { position: absolute; right: 165px; top: 0; display: flex; height: 26px; }
  .topbar .links a { color: #555; text-decoration: none; display: flex; align-items: center; gap: 4px; padding: 0 7px; border-left: 1px solid #e0e0e0; }
  .topbar .links a:last-child { border-right: 1px solid #e0e0e0; }
  .dot { width: 9px; height: 9px; border-radius: 50%; background: var(--blue-deep); display: inline-block; }

  .header { height: 48px; position: relative; }
  .brand { position: absolute; left: 166px; top: 14px; display: flex; align-items: center; gap: 6px; font-weight: 700; font-size: 17px; color: var(--blue); }
  .brand i { width: 14px; height: 14px; background: var(--blue-bright); border-radius: 50%; display: block; }
  .nav { position: absolute; right: 165px; top: 17px; display: flex; gap: 16px; font-size: 10.5px; color: #444; }

  .hero { position: absolute; top: 74px; left: 0; width: 989px; height: 330px; }
  .hero .photo { position: absolute; inset: 0; background: linear-gradient(180deg, #b9cfe2 0%, #dfe6ec 38%, #cfc4ad 62%, #b7a88a 100%); }
  .hero svg.bands { position: absolute; inset: 0; }
  .hero-copy { position: absolute; top: 80px; left: 0; width: 989px; text-align: center; }
  .hero-copy h1 { font-weight: 900; font-size: 36px; line-height: 37px; letter-spacing: -1.6px; color: var(--blue-deep); }
  .hero-copy p { font-size: 13.5px; line-height: 16px; color: #222; margin-top: 6px; }
  .hero-copy .cta { display: inline-block; margin-top: 9px; background: #555; color: #fff; font-size: 15px; padding: 4px 13px; }

  .solutions { position: absolute; top: 464px; left: 166px; width: 658px; display: flex; }
  .solution { width: 168px; text-align: center; }
  .solution .icon { width: 71px; height: 71px; border-radius: 50%; background: var(--blue); margin: 0 auto; display: flex; align-items: center; justify-content: center; }
  .solution h3 { font-weight: 400; font-size: 11.5px; line-height: 13px; margin-top: 14px; height: 30px; }
  .btn { display: inline-block; background: var(--btn); color: #fff; font-size: 10px; padding: 5px 11px; border: 1px solid #444; }

  .integrate { position: absolute; top: 661px; left: 0; width: 989px; height: 160px; background: var(--light); border-top: 1px solid #e6e6e6; text-align: center; }
  .integrate h2 { font-weight: 700; font-size: 24px; color: var(--blue); margin-top: 25px; line-height: 26px; }
  .integrate .sub { font-size: 12px; color: #333; margin-top: 3px; }
  .integrate h4 { font-weight: 500; font-size: 16px; color: var(--blue-bright); margin-top: 9px; }
  .integrate .apis { font-size: 13px; color: #222; margin-top: 3px; }
  .integrate svg { position: absolute; left: 0; top: 113px; }

  .features { position: absolute; top: 858px; left: 166px; width: 658px; display: flex; justify-content: space-between; }
  .feature { width: 110px; text-align: center; font-size: 10.5px; line-height: 13px; color: #333; }
  .feature svg { display: block; margin: 0 auto 12px; }

  .footer { position: absolute; top: 1002px; left: 0; width: 989px; height: 198px; background: var(--footer); }
  .footer h5 { font-weight: 400; font-size: 16px; color: var(--footer-head); }
  .col { position: absolute; top: 30px; }
  .about { left: 166px; width: 165px; }
  .about p { font-size: 8px; line-height: 13.5px; color: var(--footer-text); margin-top: 14px; }
  .posts { left: 347px; }
  .posts li { list-style: none; margin-top: 9px; font-size: 9.5px; color: var(--footer-text); }
  .posts li:first-child { margin-top: 16px; }
  .posts small { display: block; font-size: 7.5px; color: #999; }
  .social { left: 477px; }
  .social .circles { display: flex; gap: 5px; margin-top: 12px; }
  .social .circles span { width: 31px; height: 31px; border-radius: 50%; display: block; }
  .help { left: 657px; width: 168px; }
  .help .field { height: 23px; background: #333; border: 1px solid #2a2a2a; margin-top: 5px; font-size: 9px; color: #888; padding: 6px 8px; }
  .help .field:first-of-type { margin-top: 11px; }
  .help .or { text-align: center; font-size: 9px; color: #aaa; margin: 4px 0 -2px; }
  .help .submit { display: inline-block; margin-top: 7px; background: var(--blue); color: #3a3a3a; font-size: 10px; padding: 5px 12px; }
</style>
</head>
<body>

<div class="topbar">
  <div class="search"><svg width="11" height="11" viewBox="0 0 12 12"><circle cx="5" cy="5" r="3.8" fill="none" stroke="#999" stroke-width="1.6"/><path d="M8 8l3.2 3.2" stroke="#999" stroke-width="1.8"/></svg></div>
  <div class="phone"><svg width="6" height="10" viewBox="0 0 6 10"><path d="M1 1h2v8H1z" fill="none" stroke="#999"/></svg>+61 80 000 4127</div>
  <div class="social-mini"><span></span><span></span><span></span><span class="red"></span><span class="red"></span><span class="orange"></span></div>
  <div class="links">
    <a><i class="dot"></i>About Korvane</a>
    <a><i class="dot"></i>Register</a>
    <a><i class="dot"></i>Login</a>
  </div>
</div>

<header class="header">
  <div class="brand"><i></i>Korvane</div>
  <nav class="nav"><span>Home</span><span>Personal</span><span>Small Business</span><span>Business &amp; Enterprise</span><span>News, Sport &amp; Lifestyle</span></nav>
</header>

<section class="hero">
  <div class="photo" role="img" aria-label="Photo of a quarry and construction site with a concrete plant and conveyor under a bright sky"></div>
  <svg class="bands" width="989" height="330" viewBox="0 0 989 330">
    <polygon points="0,0 420,0 0,38" fill="#0a6bbf"/>
    <polygon points="0,6 360,0 0,64" fill="#00a3e8" opacity=".85"/>
    <polygon points="0,28 220,12 0,64" fill="#5cc6f2" opacity=".7"/>
    <polygon points="0,318 989,250 989,330 0,330" fill="#0050a0"/>
    <polygon points="0,322 989,276 989,330 0,330" fill="#0a6bbf"/>
    <polygon points="0,326 989,296 989,330 0,330" fill="#00a3e8"/>
    <polygon points="0,330 989,322 989,330" fill="#fff"/>
  </svg>
  <div class="hero-copy">
    <h1>Mining &amp; Construction<br>Solutions</h1>
    <p>KUA For Mining And Construction Is A High-availability<br>Mobile Messaging Solution</p>
    <span class="cta">READ MORE</span>
  </div>
</section>

<section class="solutions">
  <div class="solution">
    <div class="icon"><svg width="40" height="40" viewBox="0 0 40 40" fill="none" stroke="#fff" stroke-width="2.4"><rect x="14" y="8" width="12" height="24" rx="2"/><path d="M9 12q-4 8 0 16M31 12q4 8 0 16M5 9q-6 11 0 22M35 9q6 11 0 22"/></svg></div>
    <h3>Telemetry, Remote Monitoring<br>and “Wake Up” SMS</h3>
    <span class="btn">Learn More</span>
  </div>
  <div class="solution">
    <div class="icon"><svg width="36" height="40" viewBox="0 0 36 40"><path d="M18 3l14 5v11c0 9-6 15-14 18C10 34 4 28 4 19V8z" fill="#fff"/><path d="M18 10v12H10v-9zM18 22h8c0 5-3 8-8 10z" fill="#0a6bbf"/></svg></div>
    <h3>Worker Safety &amp; Incident<br>Broadcast Notification</h3>
    <span class="btn">Learn More</span>
  </div>
  <div class="solution">
    <div class="icon"><svg width="40" height="40" viewBox="0 0 40 40" fill="#fff"><circle cx="11" cy="9" r="4"/><path d="M4 22q0-7 7-7t7 7z"/><circle cx="29" cy="22" r="4"/><path d="M22 35q0-7 7-7t7 7z"/><path d="M22 8h8l-3-3M18 28h-7l3 3" stroke="#fff" stroke-width="2" fill="none"/></svg></div>
    <h3>Staffing, Shifts &amp;<br>Contractor Redeployment</h3>
    <span class="btn">Learn More</span>
  </div>
  <div class="solution">
    <div class="icon"><svg width="40" height="40" viewBox="0 0 40 40" fill="#fff"><circle cx="20" cy="8" r="3.5"/><path d="M14 18q0-5 6-5t6 5z"/><circle cx="9" cy="25" r="3.5"/><path d="M3 35q0-5 6-5t6 5z"/><circle cx="31" cy="25" r="3.5"/><path d="M25 35q0-5 6-5t6 5z"/><circle cx="20" cy="26" r="3.5"/><path d="M14 36q0-5 6-5t6 5z"/></svg></div>
    <h3>Dispatch &amp; Remote<br>Worker Logistics</h3>
    <span class="btn">Learn More</span>
  </div>
</section>

<section class="integrate">
  <h2>READY TO INTEGRATE</h2>
  <p class="sub">Custom &amp; Proprietory Systems Integration</p>
  <h4>APIs Include</h4>
  <p class="apis">HTTP/S, SMTP, WSDL, SMPP, JAVA, .NET</p>
  <svg width="989" height="47" viewBox="0 0 989 47">
    <polygon points="0,0 989,14 989,47 0,47" fill="#00a3e8"/>
    <polygon points="0,20 989,20 989,47 0,47" fill="#0a6bbf"/>
    <polygon points="0,42 989,22 989,47 0,47" fill="#fff"/>
  </svg>
</section>

<section class="features">
  <div class="feature"><svg width="30" height="44" viewBox="0 0 30 44"><rect x="3" y="2" width="20" height="40" rx="3" fill="#1e9be0"/><rect x="6" y="7" width="14" height="28" fill="#fff"/><rect x="11" y="15" width="16" height="11" fill="#0a6bbf"/><path d="M13 26v5l4-5z" fill="#0a6bbf"/></svg>Powerful Mobile<br>Messaging Platform</div>
  <div class="feature"><svg width="46" height="50" viewBox="0 0 46 50" fill="none" stroke="#1e9be0" stroke-width="2.6"><rect x="3" y="2" width="20" height="36" rx="2"/><rect x="23" y="14" width="20" height="34" rx="2" fill="#fff"/><path d="M7 8h12M27 20h12"/></svg>Integrated 2-Way<br>SMS, MMS, Email</div>
  <div class="feature"><svg width="48" height="46" viewBox="0 0 48 46" fill="#1e9be0"><path d="M6 40l22-22 4 4-22 22z"/><path d="M18 6l12-4 14 14-6 6-10-10-6 2z"/><path d="M30 30l10 12 4-4-12-10z"/><path d="M4 8a9 9 0 0112-4l-5 6 3 3 6-5a9 9 0 01-4 12z"/></svg>Highly<br>Configurable</div>
  <div class="feature"><svg width="44" height="52" viewBox="0 0 44 52"><circle cx="20" cy="20" r="13" fill="#1e9be0"/><g fill="#1e9be0"><rect x="17" y="2" width="6" height="7"/><rect x="17" y="31" width="6" height="7"/><rect x="2" y="17" width="7" height="6"/><rect x="31" y="17" width="7" height="6"/></g><circle cx="20" cy="20" r="5" fill="#fff"/><circle cx="34" cy="40" r="8" fill="#0a6bbf"/><circle cx="34" cy="40" r="3" fill="#fff"/></svg>Setup<br>Assistance</div>
  <div class="feature"><svg width="44" height="52" viewBox="0 0 44 52"><path d="M24 2L6 30h12l-6 20 14-20" fill="#1e9be0"/><circle cx="28" cy="36" r="11" fill="#fff" stroke="#0a6bbf" stroke-width="3"/><path d="M22 36l5 5 8-9" fill="none" stroke="#0a6bbf" stroke-width="3"/></svg>Ready to use in<br>10 days</div>
  <div class="feature"><svg width="48" height="48" viewBox="0 0 48 48" fill="none" stroke="#1e9be0" stroke-width="3.4"><circle cx="24" cy="24" r="21"/><path d="M24 10v14h11" stroke-width="4.5"/></svg>Support<br>24x7x365</div>
</section>

<footer class="footer">
  <div class="col about">
    <h5>About Korvane</h5>
    <p>Summit is a Multi-Purpose SiteForge business theme. Perfect for corporates like financial institutions, law firms and education establishments.</p>
  </div>
  <div class="col posts">
    <h5>Popular Posts</h5>
    <ul>
      <li>The Four Suburbs<small>06 Aug 2013</small></li>
      <li>The National Guardians<small>06 Aug 2013</small></li>
    </ul>
  </div>
  <div class="col social">
    <h5>We’re Social</h5>
    <div class="circles"><span style="background:#3b5b9a"></span><span style="background:#29a9e1"></span><span style="background:#1a77a8"></span><span style="background:#dc4a38"></span></div>
  </div>
  <div class="col help">
    <h5>Let Us Help You</h5>
    <div class="field">Name</div>
    <div class="field">Email</div>
    <div class="or">or</div>
    <div class="field">Phone Number</div>
    <span class="submit">SUBMIT</span>
  </div>
</footer>

</body>
</html>
```